Brasko Construction Business Card

I need a business card design for my company.
We are a construction/machinery company.
I would like to see my logo on the front of the card and my details on the other side
I would like the card to be black or dark grey in colour,with my logo as i send it or modified with a lighter blue colour
I would like to see the design kept fairly simple,but eye catching at the same time
Industry/Entity Type
Business
Contact Information for Business Card
Name
Phone Number
Address
Email
Colors
00a990
1b1b1b
000000
474747
ececec

```html
<!DOCTYPE html>
<html lang="en">
<head>
<meta charset="utf-8">
<title>Brasko Construction Business Card</title>
<link rel="stylesheet" href="https://fonts.googleapis.com/css2?family=Montserrat:wght@400;700&display=swap">
<style>
  :root {
    --teal: #00a990;
    --teal-deep: #009a83;
    --ink: #1b1b1b;
    --black: #000000;
    --slate: #474747;
    --paper: #ffffff;
    --light: #ececec;
  }
  * { margin: 0; padding: 0; box-sizing: border-box; }
  html, body {
    width: 1124px;
    height: 1200px;
    overflow: hidden;
    background: var(--paper);
    font-family: "Montserrat", Arial, sans-serif;
  }
  .canvas {
    position: relative;
    width: 1124px;
    height: 1200px;
  }
  .card {
    position: absolute;
    left: 114px;
    width: 895px;
    height: 497px;
    overflow: hidden;
  }
  .card-front {
    top: 92px;
    background: var(--teal);
  }
  .card-front .corner {
    position: absolute;
    inset: 0;
    width: 895px;
    height: 497px;
  }
  .machine-art {
    position: absolute;
    left: 0;
    top: 74px;
    width: 535px;
    height: 320px;
    background: linear-gradient(135deg, var(--teal-deep), var(--teal));
    border-radius: 0 60px 20px 0;
  }
  .brand {
    position: absolute;
    left: 620px;
    top: 380px;
    width: 260px;
    display: flex;
    align-items: center;
    gap: 10px;
    color: var(--teal);
    font-weight: 700;
    font-size: 22px;
    line-height: 1.15;
    text-transform: uppercase;
    letter-spacing: 1px;
  }
  .brand-mark {
    flex: none;
    width: 14px;
    height: 14px;
    background: var(--teal);
  }
  .card-back {
    top: 610px;
    background: var(--teal);
  }
  .name-band {
    position: absolute;
    left: 0;
    top: 0;
    width: 100%;
    height: 265px;
    background: var(--ink);
  }
  .person-name {
    position: absolute;
    top: 166px;
    width: 100%;
    text-align: center;
    color: var(--paper);
    font-size: 32px;
    font-weight: 400;
    letter-spacing: 0.5px;
  }
  .contact {
    position: absolute;
    top: 358px;
    width: 100%;
    text-align: center;
    color: var(--black);
    font-size: 32px;
    font-weight: 400;
    line-height: 39px;
  }
</style>
</head>
<body>
<div class="canvas">
  <section class="card card-front">
    <div class="machine-art" role="img" aria-label="Line illustration of an excavator arm and bucket"></div>
    <svg class="corner" viewBox="0 0 895 497" aria-hidden="true">
      <polygon points="824,0 895,0 490,497 476,497" fill="var(--slate)"/>
      <polygon points="895,0 895,497 490,497" fill="var(--ink)"/>
    </svg>
    <div class="brand">
      <span class="brand-mark"></span>
      <span class="brand-name">Brasko Construction</span>
    </div>
  </section>

  <section class="card card-back">
    <div class="name-band">
      <p class="person-name">Name xxxxxxxxx</p>
    </div>
    <div class="contact">
      <p class="address">address : xxx134 xxxxxxx</p>
      <p class="email">Email : office@braskobuild.com</p>
    </div>
  </section>
</div>
</body>
</html>
```